Copperline Business Management Business Card Design Project

I have a new business called Copperline Business Management Limited. We provide business services for the UK for areas which include

Mentoring / Coaching
Interim Management
Non Executive Director / Chairman placement
Angel Investment support
Merger & Acquisition advice
Selling your business advice

I would like a background colour on the logo, a logo and our company name on the logo if possible.

I am open to colours but we want to portray a strong safe business with credibility

The business card design must match that of the logo design
Updates

Target Market(s)

SME and Medium size businesses with the owners, MD's, CEO or senior management as the target audiabce

Industry/Entity Type

Business

Requirements
Must have
• Match the logo design.
Look professional and quality
Should not have
• Old style text and colours
Poor logos depicting money

```html
<!DOCTYPE html>
<html lang="en">
<head>
<meta charset="utf-8">
<title>Copperline Business Management – Business Card</title>
<link rel="stylesheet" href="https://fonts.googleapis.com/css2?family=Cinzel:wght@500&family=Lato:wght@400;700&display=swap">
<style>
  :root {
    --stage: #ebe8e3;
    --charcoal: #454545;
    --ink: #3a3a3a;
    --green: #5f9e63;
    --white: #ffffff;
  }
  * { margin: 0; padding: 0; box-sizing: border-box; }
  html, body { width: 1200px; height: 800px; overflow: hidden; }
  body {
    background: var(--stage);
    position: relative;
    font-family: "Lato", Arial, sans-serif;
  }
  .card {
    position: absolute;
    width: 488px;
    height: 320px;
    box-shadow: 0 3px 10px rgba(0,0,0,0.18);
    overflow: hidden;
  }
  .card--front { left: 286px; top: 88px; background: var(--charcoal); }
  .card--back  { left: 289px; top: 424px; background: var(--white); }

  .brand {
    position: absolute;
    display: flex;
    align-items: center;
    gap: 16px;
  }
  .brand__square {
    width: 62px;
    height: 62px;
    background: var(--green);
    flex: none;
  }
  .brand__name {
    font-family: "Cinzel", Georgia, serif;
    font-weight: 500;
    line-height: 1;
  }
  .brand__title { display: block; font-size: 31px; letter-spacing: 2px; }
  .brand__sub { display: block; font-size: 11.5px; letter-spacing: 0.4px; margin-top: 7px; }
  .card--front .brand { left: 84px; top: 124px; }
  .card--front .brand__name { color: var(--white); }
  .card--back .brand { left: 33px; top: 42px; }
  .card--back .brand__name { color: var(--ink); }

  .services {
    position: absolute;
    left: 0; right: 0; top: 248px;
    text-align: center;
    color: var(--white);
    font-size: 12.5px;
    line-height: 18px;
  }
  .services .sep { color: var(--green); }

  .person { position: absolute; left: 33px; top: 164px; }
  .person__name {
    font-family: "Cinzel", Georgia, serif;
    font-weight: 500;
    color: var(--green);
    font-size: 16px;
    letter-spacing: 0.6px;
  }
  .person__role { color: var(--ink); font-size: 12px; font-weight: 700; margin-top: 2px; }

  .contacts {
    position: absolute; left: 33px; top: 231px;
    list-style: none;
    font-size: 12px; color: var(--ink); line-height: 18px;
  }
  .contacts li { display: flex; align-items: center; gap: 6px; }
  .contacts svg { width: 13px; height: 13px; fill: var(--green); flex: none; }

  .address {
    position: absolute; right: 32px; top: 231px;
    text-align: right; font-size: 12px; color: var(--ink); line-height: 18px;
    font-style: normal;
  }
  .address__company { color: var(--green); }

  .footer-band { position: absolute; left: 0; bottom: 0; width: 488px; height: 14px; }
</style>
</head>
<body>

<section class="card card--front" aria-label="Card front">
  <div class="brand">
    <span class="brand__square"></span>
    <span class="brand__name">
      <span class="brand__title">COPPERLINE</span>
      <span class="brand__sub">BUSINESS MANAGEMENT LIMITED</span>
    </span>
  </div>
  <p class="services">
    Mentoring / Coaching <span class="sep">|</span> Interim Management<br>
    Non Executive Director / Chairman Placement <span class="sep">|</span> Angel Investment Support<br>
    Merger &amp; Acquisition Advice <span class="sep">|</span> Selling your Business Advice
  </p>
</section>

<section class="card card--back" aria-label="Card back">
  <div class="brand">
    <span class="brand__square"></span>
    <span class="brand__name">
      <span class="brand__title">COPPERLINE</span>
      <span class="brand__sub">BUSINESS MANAGEMENT LIMITED</span>
    </span>
  </div>

  <div class="person">
    <p class="person__name">MARTIN HALE</p>
    <p class="person__role">General Manager</p>
  </div>

  <ul class="contacts">
    <li>
      <svg viewBox="0 0 24 24" aria-hidden="true"><path d="M6.6 10.8a15.1 15.1 0 0 0 6.6 6.6l2.2-2.2c.3-.3.7-.4 1-.2 1.1.4 2.3.6 3.6.6.6 0 1 .4 1 1V20c0 .6-.4 1-1 1A17 17 0 0 1 3 4c0-.6.4-1 1-1h3.5c.6 0 1 .4 1 1 0 1.3.2 2.5.6 3.6.1.3 0 .7-.2 1z"/></svg>
      020 7946 0321
    </li>
    <li>
      <svg viewBox="0 0 24 24" aria-hidden="true"><path d="M2 5h20v14H2z M3.5 6.5 12 13l8.5-6.5" stroke="#fff" stroke-width="1.4"/></svg>
      martinh@copperlinebusiness.co.uk
    </li>
    <li>
      <svg viewBox="0 0 24 24" aria-hidden="true"><circle cx="12" cy="12" r="10"/><path d="M2 12h20M12 2c3 3 3 17 0 20M12 2c-3 3-3 17 0 20" stroke="#fff" stroke-width="1.3" fill="none"/></svg>
      www.copperlinebusiness.co.uk
    </li>
  </ul>

  <address class="address">
    <span class="address__company">Copperline Business Management Ltd.</span><br>
    Suite 40, Mill Lane, Harrowby,<br>
    UK 67890
  </address>

  <svg class="footer-band" viewBox="0 0 488 14" aria-hidden="true">
    <polygon points="0,0 286,0 280,14 0,14" fill="var(--charcoal)"/>
    <polygon points="292,0 488,0 488,14 286,14" fill="var(--green)"/>
  </svg>
</section>

</body>
</html>
```